Zorvath GmbH banner ad

Banner ad for Facebook Our company name (logo) Title: Transporter and bus rental Text: Without deposit, super prices

Target Market(s)

Rental

Requirements
Must have
• LOGO from us, Evt. A pair of transporters in the picture

```html
<!DOCTYPE html>
<html lang="de">
<head>
<meta charset="utf-8">
<title>Zorvath GmbH – Transporter und Bus Vermietung</title>
<link rel="stylesheet" href="https://fonts.googleapis.com/css2?family=Poppins:wght@300;500;600&display=swap">
<style>
  :root {
    --navy: #07087a;
    --brand-blue: #1f3a9e;
    --edge-blue: #8fb6e6;
    --white: #ffffff;
    --photo-sky: #dfe2e6;
    --photo-van: #eef0f2;
    --photo-mid: #c3c7cc;
    --photo-ground: #5c6066;
  }
  html, body {
    margin: 0;
    padding: 0;
    overflow: hidden;
    background: var(--white);
  }
  .banner {
    position: relative;
    width: 1200px;
    height: 444px;
    overflow: hidden;
    font-family: "Poppins", sans-serif;
  }
  .van-photo {
    position: absolute;
    inset: 0;
    background: linear-gradient(180deg, var(--photo-sky) 0%, var(--photo-van) 30%, var(--photo-mid) 65%, var(--photo-ground) 100%);
  }
  .panel {
    position: absolute;
    inset: 0;
  }
  .brand-name {
    position: absolute;
    left: 36px;
    top: 128px;
    margin: 0;
    color: var(--brand-blue);
    font-weight: 600;
    font-size: 34px;
    line-height: 48px;
    white-space: nowrap;
  }
  .brand-phone {
    position: absolute;
    left: 36px;
    top: 214px;
    margin: 0;
    display: flex;
    align-items: center;
    gap: 12px;
    color: var(--brand-blue);
    font-weight: 600;
    font-size: 30px;
    line-height: 40px;
    white-space: nowrap;
  }
  .brand-phone svg {
    width: 26px;
    height: 26px;
    fill: var(--brand-blue);
  }
  .headline {
    position: absolute;
    left: 662px;
    width: 470px;
    top: 99px;
    margin: 0;
    text-align: center;
    color: var(--white);
    font-weight: 600;
    font-size: 50px;
    line-height: 70px;
    white-space: nowrap;
  }
  .tagline {
    position: absolute;
    left: 620px;
    width: 550px;
    top: 279px;
    margin: 0;
    text-align: center;
    color: var(--white);
    font-weight: 300;
    font-size: 40px;
    line-height: 48px;
    white-space: nowrap;
  }
</style>
</head>
<body>
<div class="banner">
  <div class="van-photo" role="img" aria-label="Foto: weißer Transporter mit Firmenbeschriftung auf einem Parkplatz"></div>

  <p class="brand-name">Zorvath GmbH</p>
  <p class="brand-phone">
    <svg viewBox="0 0 24 24" aria-hidden="true"><path d="M6.6 10.8a15.1 15.1 0 0 0 6.6 6.6l2.2-2.2a1 1 0 0 1 1-.25 11.4 11.4 0 0 0 3.6.57 1 1 0 0 1 1 1V20a1 1 0 0 1-1 1A17 17 0 0 1 3 4a1 1 0 0 1 1-1h3.5a1 1 0 0 1 1 1c0 1.25.2 2.45.57 3.6a1 1 0 0 1-.25 1z"/></svg>
    0123.456.789
  </p>

  <svg class="panel" width="1200" height="444" viewBox="0 0 1200 444" aria-hidden="true">
    <polygon points="697,0 1200,0 1200,444 522,444" fill="var(--navy)"/>
    <line x1="693" y1="0" x2="518" y2="444" stroke="var(--edge-blue)" stroke-width="5"/>
  </svg>

  <h1 class="headline">Transporter und<br>Bus Vermietung</h1>
  <p class="tagline">Ohne Kaution, Superpreise</p>
</div>
</body>
</html>
```